Redesign of page from emergency manual

Please redesign this PDF to look better. Please don't include any stock photos. It must be legible. Making some words bold is probably a good idea.

Here are some things I like :

https://tarrowbooks.com.au/collections/frontpage/products/the-plk-v2-ebook

https://img-cd.vostramediafiles.com/qa-ejkwPLOTYY_SuCKbZNu411Qwgjv8YssPxEdzXN93hDkSRjLXK8WmfgbmrJW4ZZ3yUPK=w1052-h592-rw

```html
<!DOCTYPE html>
<html lang="en">
<head>
<meta charset="utf-8">
<title>Hypertension, Acute</title>
<link rel="stylesheet" href="https://fonts.googleapis.com/css2?family=Noto+Sans:ital,wght@0,400;0,700;0,800;1,400&display=swap">
<style>
  :root {
    --cyan: #6aeefc;
    --ink: #000;
    --text: #1a1a1a;
    --page: #fff;
    --backdrop: #e0e0e0;
    --yellow: #fef0a6;
    --yellow-light: #fff7d6;
    --grey-band: #d2d2d2;
    --grey-row: #f2f2f2;
    --alert: #e0201f;
  }
  * { box-sizing: border-box; margin: 0; padding: 0; }
  html, body { width: 1200px; height: 1200px; overflow: hidden; }
  body {
    background: var(--backdrop);
    font-family: "Noto Sans", sans-serif;
    color: var(--text);
    position: relative;
  }
  .sheet {
    position: absolute; left: 109px; top: 221px;
    width: 982px; height: 758px;
    background: var(--page);
  }
  .title-band {
    position: absolute; left: 0; top: 0; width: 100%; height: 89px;
    background: var(--cyan);
    display: flex; align-items: center; justify-content: center;
  }
  .title-band h1 { font-size: 47px; font-weight: 800; color: var(--ink); letter-spacing: 0.5px; }
  .subtitle-tab { position: absolute; left: 89px; top: 89px; width: 802px; height: 45px; }
  .subtitle-tab svg { position: absolute; inset: 0; }
  .subtitle-tab p {
    position: absolute; inset: 0; display: flex; align-items: center; justify-content: center;
    font-size: 18px; font-weight: 700; color: var(--ink); padding-bottom: 4px;
  }

  .left-col { position: absolute; left: 53px; top: 162px; width: 360px; }
  .intro { font-size: 15.5px; line-height: 21px; }
  .checks { list-style: none; margin-top: 8px; }
  .checks li { position: relative; padding-left: 23px; font-size: 15.5px; line-height: 21px; margin-bottom: 9px; }
  .checks li b { font-weight: 700; }
  .checks .mark { position: absolute; left: 0; top: 0; font-weight: 700; }
  .checks em { display: block; font-size: 11.5px; line-height: 16px; margin-top: 1px; }

  .bp-table { position: absolute; left: 53px; top: 356px; width: 358px; }
  .bp-head { position: relative; height: 22px; }
  .bp-head svg { position: absolute; inset: 0; }
  .bp-head span {
    position: absolute; inset: 0; display: flex; align-items: center; justify-content: center;
    font-size: 13px; font-weight: 700; color: var(--ink);
  }
  .bp-head i { color: var(--alert); font-style: normal; }
  .bp-grid { display: grid; grid-template-columns: 76px 92px 92px 92px; gap: 0 1px; border-bottom: 1px solid var(--cyan); padding: 3px 0 4px; }
  .bp-grid div { height: 22px; display: flex; align-items: center; justify-content: center; font-size: 12.5px; font-weight: 700; }
  .bp-grid .label { font-weight: 400; font-size: 11.5px; justify-content: flex-end; padding-right: 12px; }
  .bp-grid .age { background: var(--cyan); height: 18px; margin: 2px 0; }

  .differential { position: absolute; left: 53px; top: 473px; width: 353px; }
  .differential h2 {
    background: var(--grey-band); height: 31px; display: flex; align-items: center; justify-content: center;
    font-size: 16px; font-weight: 700; color: var(--ink);
  }
  .differential ul { list-style: none; margin-top: 4px; }
  .differential li { position: relative; padding: 0 6px 0 35px; font-size: 15.5px; line-height: 21px; min-height: 22px; display: flex; flex-direction: column; justify-content: center; }
  .differential li::before { content: "◦"; position: absolute; left: 21px; top: 50%; transform: translateY(-52%); font-size: 13px; }
  .differential li:nth-child(even) { background: var(--grey-row); }
  .differential li em { font-size: 11.5px; line-height: 16px; }
  .differential li.tall { min-height: 40px; }

  .drug-panel { position: absolute; left: 455px; top: 166px; width: 481px; height: 557px; background: var(--yellow); }
  .caution-icon { position: absolute; left: 26px; top: 19px; width: 60px; height: 52px; }
  .caution-text { position: absolute; left: 99px; top: 18px; width: 370px; font-size: 15.5px; line-height: 21px; }
  .caution-text strong { font-size: 18px; font-weight: 800; color: var(--ink); }
  .caution-text .star { color: var(--alert); font-weight: 700; font-size: 18px; }
  .consult { position: absolute; left: 0; top: 154px; width: 100%; padding-left: 4px; text-align: center; font-size: 14.5px; font-weight: 700; color: var(--ink); }

  .tabs { position: absolute; left: 0; top: 200px; width: 481px; height: 31px; }
  .tabs svg { position: absolute; inset: 0; }
  .tab-label { position: absolute; top: 0; height: 31px; display: flex; align-items: center; color: #fff; font-size: 16px; }
  .tab-label.action { left: 34px; font-weight: 700; }
  .tab-label.drug { left: 232px; }
  .tab-label.drug b { font-weight: 700; margin-right: 5px; }

  .drug-rows { position: absolute; left: 0; top: 231px; width: 481px; }
  .drug-row { display: grid; grid-template-columns: 132px 1fr; }
  .drug-row.light { background: var(--yellow-light); }
  .drug-row .action { font-size: 12px; line-height: 15px; padding: 17px 0 0 16px; }
  .dose-group { padding: 6px 0; }
  .dose-group + .dose-group { border-top: 1px solid #444; }
  .dose-line { display: grid; grid-template-columns: 140px 58px 84px 1fr; align-items: baseline; min-height: 17px; }
  .dose-line .name { font-size: 12px; font-weight: 700; line-height: 15px; color: var(--ink); }
  .dose-line .name small { font-size: 7.5px; font-weight: 400; font-style: italic; }
  .dose-line .sub { font-size: 12px; font-style: italic; padding-left: 19px; }
  .dose-line .then { font-size: 12px; font-style: italic; text-align: right; padding-right: 8px; }
  .dose-line .dose { font-size: 12.5px; font-weight: 700; text-align: right; color: var(--ink); }
  .dose-line .unit { font-size: 7.5px; padding-left: 5px; }
  .dose-line .note { font-size: 7.5px; font-weight: 700; padding-left: 3px; }
</style>
</head>
<body>
  <article class="sheet">
    <header class="title-band"><h1>Hypertension, Acute</h1></header>
    <div class="subtitle-tab">
      <svg width="802" height="45" viewBox="0 0 802 45">
        <path d="M2 0 L40 38 Q47 44 58 44 L744 44 Q755 44 762 38 L800 0" fill="#fff" stroke="#6aeefc" stroke-width="3"/>
      </svg>
      <p>Sustained high blood pressure refractory to treating reversible causes</p>
    </div>

    <section class="left-col">
      <p class="intro">In pediatrics, hypertension is almost always treated by addressing likely causes such as light anesthesia or measurement error:</p>
      <ol class="checks">
        <li><span class="mark">a.</span><b>Ensure correct BP cuff size</b>: cuff bladder width ~ 40% of limb circumference</li>
        <li><span class="mark">b.</span><b>Ensure arterial line transducer</b> is at level of heart<em>Consider placing arterial line if not already present</em></li>
      </ol>
    </section>

    <section class="bp-table">
      <div class="bp-head">
        <svg width="358" height="22" viewBox="0 0 358 22">
          <path d="M0 0 L358 0 L342 16 Q336 22 326 22 L32 22 Q22 22 16 16 Z" fill="#6aeefc"/>
        </svg>
        <span>Hypertensive Blood Pressure Range<i>*</i></span>
      </div>
      <div class="bp-grid">
        <div class="label">Systolic</div><div>&gt;97</div><div>&gt;105</div><div>&gt;113</div>
        <div class="label">Age (yr)</div><div class="age">NEWBORN</div><div class="age">1-3</div><div class="age">4-15</div>
        <div class="label">Diastolic</div><div>&gt;70</div><div>&gt;61</div><div>&gt;86</div>
      </div>
    </section>

    <section class="differential">
      <h2>Consider Differential (Partial)</h2>
      <ul>
        <li class="tall"><span>Light anesthesia <em>(consider vaporizer or</em></span><em>infusion pump empty or malfunctioning)</em></li>
        <li>Hypercarbia</li>
        <li>Hypoxemia</li>
        <li class="tall">Arterial line transducer too low or BP cuff too small</li>
        <li>Withdrawal (EtOH or opioid)</li>
        <li>Thyroid Storm</li>
        <li>Pheochromocytoma</li>
        <li>Drug Error</li>
      </ul>
    </section>

    <section class="drug-panel">
      <svg class="caution-icon" viewBox="0 0 60 52" aria-hidden="true">
        <path d="M30 3 L57 47 Q58 50 55 50 L5 50 Q2 50 3 47 Z" fill="none" stroke="#000" stroke-width="4" stroke-linejoin="round"/>
        <rect x="27" y="17" width="6" height="19" rx="1" fill="#000"/>
        <rect x="27" y="39" width="6" height="6" rx="1" fill="#000"/>
      </svg>
      <p class="caution-text"><span class="star">*</span><strong>CAUTION</strong>: Anti-hypertensive drugs are almost never needed for routine pediatric cases. These medications are used almost exclusively for specialized cardiac, neurosurgical, or endocrine (pheochromocytoma) cases.</p>
      <p class="consult">Consult an expert before use • Rule-out increased ICP.</p>

      <div class="tabs">
        <svg width="481" height="31" viewBox="0 0 481 31">
          <path d="M0 31 L26 6 Q32 0 42 0 L96 0 Q104 0 110 6 L131 31 Z" fill="#000"/>
          <path d="M133 31 L158 6 Q164 0 174 0 L436 0 Q446 0 452 6 L481 31 Z" fill="#000"/>
        </svg>
        <span class="tab-label action">ACTION</span>
        <span class="tab-label drug"><b>DRUG</b>(IV DOSING)</span>
      </div>

      <div class="drug-rows">
        <div class="drug-row light" style="height:102px">
          <p class="action">Direct smooth muscle relaxation</p>
          <div>
            <div class="dose-group" style="padding-top:9px">
              <div class="dose-line" style="align-items:center"><span class="name">Sodium<br>nitroprusside</span><span class="dose">0.5-10</span><span class="unit">MICROgrams/kg/min</span></div>
            </div>
            <div class="dose-group" style="padding-top:7px">
              <div class="dose-line"><span class="name">HydrALAZINE</span><span class="dose">0.1-0.2</span><span class="unit">mg/kg</span></div>
              <div class="dose-line"><span class="sub">(adult dose)</span><span class="dose">5-10</span><span class="unit">mg/kg</span></div>
            </div>
          </div>
        </div>

        <div class="drug-row" style="height:105px">
          <p class="action">β-Adrenergic blockade</p>
          <div>
            <div class="dose-group" style="padding-top:14px">
              <div class="dose-line"><span class="name">Esmolol</span><span class="dose">100-500</span><span class="unit">MICROgrams/kg</span><span class="note">Over 5 min,</span></div>
              <div class="dose-line"><span class="then">THEN</span><span class="dose">25-300</span><span class="unit">MICROgrams/kg/min</span></div>
            </div>
            <div class="dose-group" style="padding-top:7px">
              <div class="dose-line"><span class="name">Labetalol <small>(also a effect)</small></span><span class="dose">0.2-1</span><span class="unit">mg/kg</span><span class="note">q 10 min;</span></div>
              <div class="dose-line"><span class="sub">(INFUSION)</span><span class="dose">0.4-3</span><span class="unit">mg/kg/hour</span></div>
            </div>
          </div>
        </div>

        <div class="drug-row light" style="height:66px">
          <p class="action" style="padding-top:12px">Calcium channel blockade</p>
          <div>
            <div class="dose-group" style="padding-top:12px">
              <div class="dose-line"><span class="name">niCARdapine</span><span class="dose">0.5-5</span><span class="unit">MICROgrams/kg/min</span></div>
            </div>
            <div class="dose-group" style="padding-top:6px">
              <div class="dose-line"><span class="name">Clevidipine</span><span class="dose">0.5-3.5</span><span class="unit">MICROgrams/kg/min</span></div>
            </div>
          </div>
        </div>

        <div class="drug-row" style="height:53px">
          <p class="action" style="padding-top:10px">D1-dopamine agonist</p>
          <div>
            <div class="dose-group" style="padding-top:10px">
              <div class="dose-line"><span class="name">Fenoldopam</span><span class="dose">0.2-0.8</span><span class="unit">MICROgrams/kg/min</span></div>
            </div>
          </div>
        </div>
      </div>
    </section>
  </article>
</body>
</html>
```